Email Newsletter Banner

I require 2 new email newsletter and web banners to be made up.
I require the brand names to be included on the banner which are " Gadget Dispatch" and "Byte Wirez". I would also like some sort of imagery and also a "sign up here" button. Please see below examples:
https://fernvalepages.lumoshelf.com/
https://brightquarryhub.lumoshelf.com/
https://oakdalereads.lumoshelf.com/

```html
<!DOCTYPE html>
<html lang="en">
<head>
<meta charset="utf-8">
<title>Newsletter Banners – Final Version</title>
<link rel="stylesheet" href="https://fonts.googleapis.com/css2?family=Poppins:wght@400;500;600;700&display=swap">
<style>
  :root {
    --page: #ffffff;
    --note-red: #e8262b;
    --ink-light: #ffffff;
    --wirez-deep: #0a1c28;
    --wirez-mid: #0f3a4d;
    --wirez-glow: #1f7f9a;
    --wirez-button: #18a6cf;
    --dispatch-deep: #05080a;
    --dispatch-green: #1fae4d;
    --dispatch-blue: #1c4fa8;
    --dispatch-gold: #8a7a1a;
    --dispatch-button: #2cc15c;
  }
  * { box-sizing: border-box; margin: 0; padding: 0; }
  html, body { width: 885px; height: 1200px; overflow: hidden; background: var(--page); }
  body { position: relative; font-family: "Poppins", Arial, sans-serif; }

  .page-title {
    position: absolute; left: 44px; top: 16px;
    color: var(--note-red); font-size: 21px; font-weight: 700;
  }
  .selection-note {
    position: absolute; left: 44px; top: 478px; width: 760px;
    color: var(--note-red); font-size: 12.5px; font-weight: 600; line-height: 1.45;
  }

  .banner {
    position: absolute; left: 53px;
    display: flex; align-items: center;
    overflow: hidden; color: var(--ink-light);
  }
  .banner__imagery { position: absolute; inset: 0; }
  .banner > :not(.banner__imagery) { position: relative; }
  .banner__logo { font-weight: 600; white-space: nowrap; line-height: 1; flex-shrink: 0; }
  .banner__tagline {
    font-weight: 500; white-space: nowrap; flex: 1; min-width: 0;
    overflow: hidden; text-overflow: ellipsis;
  }
  .banner__button {
    flex-shrink: 0;
    color: var(--ink-light); font-weight: 700; letter-spacing: 0.04em;
    border-radius: 3px; white-space: nowrap;
  }

  /* brand themes */
  .banner--wirez .banner__imagery {
    background:
      radial-gradient(ellipse 30% 120% at 88% 40%, rgba(31,127,154,0.55), transparent 70%),
      radial-gradient(ellipse 25% 90% at 55% 80%, rgba(31,127,154,0.35), transparent 70%),
      linear-gradient(90deg, var(--wirez-deep), var(--wirez-mid) 55%, var(--wirez-deep));
  }
  .banner--wirez .banner__button { background: var(--wirez-button); }

  .banner--dispatch .banner__imagery {
    background:
      radial-gradient(circle at 8% 85%, rgba(31,174,77,0.55), transparent 22%),
      radial-gradient(circle at 42% 15%, rgba(28,79,168,0.55), transparent 20%),
      radial-gradient(circle at 62% 90%, rgba(138,122,26,0.5), transparent 18%),
      radial-gradient(circle at 92% 30%, rgba(31,174,77,0.45), transparent 18%),
      var(--dispatch-deep);
  }
  .banner--dispatch .banner__button { background: var(--dispatch-button); }

  /* sizes */
  .banner--large { width: 779px; height: 77px; padding: 0 22px; gap: 24px; }
  .banner--large .banner__logo { font-size: 28px; }
  .banner--large .banner__tagline { font-size: 15px; }
  .banner--large .banner__button { font-size: 13px; padding: 8px 16px; }

  .banner--medium { width: 620px; height: 62px; padding: 0 18px; gap: 18px; }
  .banner--medium .banner__logo { font-size: 22px; }
  .banner--medium .banner__tagline { font-size: 11.5px; }
  .banner--medium .banner__button { font-size: 10.5px; padding: 7px 12px; }

  .banner--small { width: 575px; height: 53px; padding: 0 16px; gap: 16px; }
  .banner--small .banner__logo { font-size: 18px; }
  .banner--small .banner__tagline { font-size: 10px; }
  .banner--small .banner__button { font-size: 10px; padding: 6px 12px; }

  /* logo lettering variants */
  .logo--caps { text-transform: uppercase; font-weight: 700; letter-spacing: 0.02em; }
  .logo--lower { text-transform: lowercase; font-weight: 700; }
  .banner--small .logo--wide { text-transform: uppercase; font-weight: 600; letter-spacing: 0.08em; font-size: 15px; }

  .option-label {
    position: absolute; left: 676px;
    color: var(--note-red); font-size: 12.5px; font-weight: 600;
  }
</style>
</head>
<body>
  <h1 class="page-title">Final Version</h1>

  <div class="banner banner--wirez banner--large" style="top:83px">
    <div class="banner__imagery" role="img" aria-label="Soft blue glowing technology background"></div>
    <span class="banner__logo">Byte Wirez</span>
    <span class="banner__tagline">Delivering the latest IT news to your inbox</span>
    <span class="banner__button">SIGN UP</span>
  </div>

  <div class="banner banner--wirez banner--medium" style="top:186px">
    <div class="banner__imagery" role="img" aria-label="Soft blue glowing technology background"></div>
    <span class="banner__logo">Byte Wirez</span>
    <span class="banner__tagline">Delivering the latest IT news to your inbox</span>
    <span class="banner__button">SIGN UP</span>
  </div>

  <div class="banner banner--dispatch banner--medium" style="top:280px">
    <div class="banner__imagery" role="img" aria-label="Dark background with coloured bokeh lights"></div>
    <span class="banner__logo">Gadget Dispatch</span>
    <span class="banner__tagline">Essential Whitepapers for IT Professionals</span>
    <span class="banner__button">SIGN UP</span>
  </div>

  <div class="banner banner--dispatch banner--large" style="top:372px">
    <div class="banner__imagery" role="img" aria-label="Dark background with coloured bokeh lights"></div>
    <span class="banner__logo">Gadget Dispatch</span>
    <span class="banner__tagline">Essential Whitepapers for IT Professionals</span>
    <span class="banner__button">SIGN UP</span>
  </div>

  <p class="selection-note">Showing different options for gadget dispatch. Please mention the mock no for the final selection for this</p>

  <div class="banner banner--dispatch banner--small" style="top:543px">
    <div class="banner__imagery" role="img" aria-label="Dark background with coloured bokeh lights"></div>
    <span class="banner__logo">Gadget Dispatch</span>
    <span class="banner__tagline">Essential Whitepapers for IT Professionals</span>
    <span class="banner__button">SIGN UP</span>
  </div>
  <span class="option-label" style="top:561px">Option 1(current design)</span>

  <div class="banner banner--dispatch banner--small" style="top:634px">
    <div class="banner__imagery" role="img" aria-label="Dark background with coloured bokeh lights"></div>
    <span class="banner__logo logo--caps">Gadget Dispatch</span>
    <span class="banner__tagline">Essential Whitepapers for IT Professionals</span>
    <span class="banner__button">SIGN UP</span>
  </div>
  <span class="option-label" style="top:652px">Option 2</span>

  <div class="banner banner--dispatch banner--small" style="top:723px">
    <div class="banner__imagery" role="img" aria-label="Dark background with coloured bokeh lights"></div>
    <span class="banner__logo logo--wide">Gadget Dispatch</span>
    <span class="banner__tagline">Essential Whitepapers for IT Professionals</span>
    <span class="banner__button">SIGN UP</span>
  </div>
  <span class="option-label" style="top:741px">Option 3</span>

  <div class="banner banner--dispatch banner--small" style="top:814px">
    <div class="banner__imagery" role="img" aria-label="Dark background with coloured bokeh lights"></div>
    <span class="banner__logo">Gadget Dispatch</span>
    <span class="banner__tagline">Essential Whitepapers for IT Professionals</span>
    <span class="banner__button">SIGN UP</span>
  </div>
  <span class="option-label" style="top:832px">Option 4</span>

  <div class="banner banner--dispatch banner--small" style="top:909px">
    <div class="banner__imagery" role="img" aria-label="Dark background with coloured bokeh lights"></div>
    <span class="banner__logo logo--lower">Gadget Dispatch</span>
    <span class="banner__tagline">Essential Whitepapers for IT Professionals</span>
    <span class="banner__button">SIGN UP</span>
  </div>
  <span class="option-label" style="top:927px">Option 5</span>

  <div class="banner banner--dispatch banner--small" style="top:1000px">
    <div class="banner__imagery" role="img" aria-label="Dark background with coloured bokeh lights"></div>
    <span class="banner__logo logo--caps">Gadget Dispatch</span>
    <span class="banner__tagline">Essential Whitepapers for IT Professionals</span>
    <span class="banner__button">SIGN UP</span>
  </div>
  <span class="option-label" style="top:1018px">Option 6</span>

  <div class="banner banner--dispatch banner--small" style="top:1092px">
    <div class="banner__imagery" role="img" aria-label="Dark background with coloured bokeh lights"></div>
    <span class="banner__logo logo--wide">Gadget Dispatch</span>
    <span class="banner__tagline">Essential Whitepapers for IT Professionals</span>
    <span class="banner__button">SIGN UP</span>
  </div>
  <span class="option-label" style="top:1110px">Option 7</span>
</body>
</html>
```